Vodka Bottle Label - Lune Vodka

I need a bottle label for a vodka I'd like to make called Lune Vodka.
I would like a label that looks elegant and fresh. I would like some mountains and colours to be red and white. Open to other colours being added but not too colourful. "Lune" means fresh, dawn in polish, i would like if mountains or something extra was added to the label too. I would like the Lune Vodka name not to be too small.
The vodka is made in australia and is 37%.

I would love to have a little bit of gold colour in the label!

I will provide the back label words when completing my decision.

i'd like to make it more simple and less european looking. More australian.

I saw a bottle like this and i did like the concept.

https://www.oakbarrelcellars.com.au/spirits/grey-vodka-range?srsltid=XqTz81mwkPLd04-hr-q7w93nfbzkgd_mR2yTpaMWxJeQ6vcbTnZsLpo

Target Market(s)

Vodka Drinkers

Industry/Entity Type

Alcohol

Colors
EB3D1F
EC4F4E
F09395
F8D3D4
FCEDEE

Requirements
Must have
• red and white colours incorporated, mountains or freshness on it.
Nice to have
• Fresh and clean look. Classy

```html
<!DOCTYPE html>
<html lang="en">
<head>
<meta charset="utf-8">
<title>Lune Vodka – Front Label</title>
<link rel="stylesheet" href="https://fonts.googleapis.com/css2?family=Merriweather:wght@400;700;900&display=swap">
<style>
  :root {
    --page-bg: #f4f4f5;
    --label-bg: #ffffff;
    --brand-red: #e52128;
    --deep-red: #8e1b20;
    --mist-light: #fcedee;
    --mist-pale: #f8d3d4;
    --mist-mid: #f09395;
    --mist-strong: #ec4f4e;
  }
  * { margin: 0; padding: 0; box-sizing: border-box; }
  html, body {
    width: 685px;
    height: 1200px;
    overflow: hidden;
    background: var(--page-bg);
  }
  .canvas {
    position: relative;
    width: 685px;
    height: 1200px;
  }
  .label {
    position: absolute;
    left: 42px;
    top: 356px;
    width: 600px;
    height: 487px;
    background: var(--label-bg);
    box-shadow: 0 1px 4px rgba(0, 0, 0, 0.18);
    font-family: "Merriweather", Georgia, serif;
    text-align: center;
  }
  .landscape {
    position: absolute;
    left: 0;
    top: 52px;
    width: 600px;
    height: 208px;
    background:
      linear-gradient(180deg,
        var(--mist-pale) 0%,
        var(--mist-mid) 18%,
        var(--mist-light) 32%,
        var(--mist-mid) 46%,
        var(--mist-light) 58%,
        var(--mist-strong) 74%,
        var(--brand-red) 90%,
        var(--mist-strong) 100%);
  }
  .brand-name {
    position: absolute;
    left: 0;
    right: 0;
    top: 262px;
    font-size: 104px;
    font-weight: 700;
    line-height: 1.1;
    color: var(--brand-red);
    letter-spacing: 1px;
  }
  .product-type {
    position: absolute;
    left: 0;
    right: 0;
    top: 374px;
    display: flex;
    justify-content: center;
    align-items: center;
    gap: 14px;
    color: var(--brand-red);
  }
  .product-type .rule {
    width: 43px;
    height: 2px;
    background: var(--brand-red);
  }
  .product-type .word {
    font-size: 29px;
    font-weight: 700;
    letter-spacing: 5px;
    line-height: 1;
  }
  .origin {
    position: absolute;
    left: 0;
    right: 0;
    top: 423px;
    font-size: 14.5px;
    line-height: 19px;
    color: var(--deep-red);
    letter-spacing: 0.3px;
  }
  .strength {
    position: absolute;
    left: 455px;
    top: 447px;
    font-size: 13px;
    color: var(--brand-red);
    white-space: nowrap;
  }
</style>
</head>
<body>
  <main class="canvas">
    <section class="label">
      <div class="landscape" role="img" aria-label="Misty red watercolour mountain ranges with pine forests in the foreground"></div>
      <h1 class="brand-name">LUNE</h1>
      <div class="product-type">
        <span class="rule"></span>
        <span class="word">VODKA</span>
        <span class="rule"></span>
      </div>
      <p class="origin">DISTILLED AND BOTTLED<br>IN AUSTRALIA</p>
      <p class="strength">37% ALC. / VOL.</p>
    </section>
  </main>
</body>
</html>
```